Menu Board 1000mmx500mm re-design

I would like to re-design exiting menu board 1000mmx500mm. Current board letters are bit to small to read. I would like to have pictures (attached) of the food offered on it and at the same time to create balance between pictures and size of the text to be easily readable. Fonts and colours are up to designer choice but prefer warm and bright colours rather anything dark.

Target Market(s)

Food industry

Industry/Entity Type

Food

Font styles to use
Other font styles liked:
• I leave font choice to designer

Colors
FFC000
F8CF3A
FAE287
FDF2CF
FEFAEE
F0912C
F2A743
F7CA91
FBE8D2
FDF5EE
EE7325
F08F49
F5BC92
FAE3D3
FDF4ED

Requirements
Must have
• Pictures + Text
Nice to have
• Balance between images and text.
Should not have
• Can't think of any

```html
<!DOCTYPE html>
<html lang="en">
<head>
<meta charset="utf-8">
<title>Menu Board</title>
<link href="https://fonts.googleapis.com/css2?family=Anton&family=Jost:wght@400;500;700&family=Permanent+Marker&display=swap" rel="stylesheet">
<style>
  :root {
    --sun: #FFC000;
    --ink: #0b0b0b;
    --paper: #ffffff;
    --cream: #FDF2CF;
    --wrap-light: #F7CA91;
    --wrap-mid: #F2A743;
    --wood: #b0703a;
    --wood-dark: #8a5128;
    --beet: #b85a6a;
    --potato: #F0912C;
  }
  html, body { margin: 0; padding: 0; overflow: hidden; }
  body { width: 1200px; height: 2400px; background: var(--sun); }
  .board {
    position: relative; width: 1200px; height: 2400px; overflow: hidden;
    background: var(--sun); font-family: "Jost", "Futura", sans-serif; color: var(--paper);
  }
  .board__shapes { position: absolute; inset: 0; }
  .title {
    position: absolute; left: 318px; top: 790px; margin: 0;
    font-family: "Permanent Marker", cursive; font-weight: 400;
    font-size: 250px; line-height: 1; color: var(--ink); letter-spacing: 4px;
  }
  .item { position: absolute; }
  .item__name {
    font-weight: 700; font-size: 38px; line-height: 1; letter-spacing: 1px; text-transform: uppercase;
  }
  .item__desc { font-weight: 400; font-size: 25px; line-height: 1.16; margin-top: 6px; }
  .item__price { position: absolute; font-weight: 700; font-size: 40px; line-height: 1; }
  .item--box .item__name { font-size: 42px; }
  .item--box .item__price { font-size: 44px; }
  .item--side .item__name { font-size: 34px; }
  .item--side .item__desc { font-size: 21px; margin-top: 4px; }
  .footer {
    position: absolute; left: 0; top: 2250px; width: 1200px; height: 150px; background: var(--paper);
    color: var(--ink);
  }
  .footer__title {
    position: absolute; left: 62px; top: 8px; margin: 0;
    font-family: "Anton", sans-serif; font-weight: 400; font-size: 140px; line-height: 1;
  }
  .sauce-list {
    position: absolute; left: 546px; top: 42px; width: 620px; margin: 0; padding: 0; list-style: none;
    display: grid; grid-template-columns: 294px 162px 164px; row-gap: 4px;
    font-weight: 700; font-size: 35px; line-height: 1; text-transform: uppercase;
  }
</style>
</head>
<body>
<main class="board">
  <svg class="board__shapes" width="1200" height="2400" viewBox="0 0 1200 2400">
    <!-- corner strokes -->
    <g fill="var(--ink)">
      <polygon points="0,0 560,0 0,300"/>
      <polygon points="110,96 580,0 200,150 0,560 0,420"/>
      <polygon points="0,560 210,160 40,560"/>
      <polygon points="235,555 560,730 575,775 250,600"/>
      <polygon points="780,115 1030,260 1040,300 800,150"/>
      <polygon points="1200,520 995,740 1200,1010 1200,930 1060,740 1200,600"/>
    </g>
    <!-- diamond frame -->
    <polygon points="665,20 1040,410 630,800 255,420" fill="none" stroke="var(--ink)" stroke-width="24"/>
    <!-- hero wrap photo -->
    <path role="img" aria-label="Photo of a grilled wrap cut in half, filled with spinach, tomato, cucumber and red onion"
          d="M230,310 Q300,200 520,190 L880,160 Q1000,210 1010,330 L1020,560 Q980,680 640,680 L300,660 Q210,620 220,480 Z"
          fill="var(--wrap-light)"/>
    <!-- arrows -->
    <g fill="var(--ink)">
      <polygon points="78,890 132,890 176,945 132,1000 78,1000 122,945"/>
      <polygon points="148,890 202,890 246,945 202,1000 148,1000 192,945"/>
      <polygon points="218,890 272,890 316,945 272,1000 218,1000 262,945"/>
    </g>
    <!-- brush banners -->
    <g fill="var(--ink)">
      <path d="M566,1082 L1116,1076 Q1126,1150 1118,1222 L560,1226 Z"/>
      <path d="M572,1232 L1126,1228 Q1134,1290 1124,1354 L566,1358 Z"/>
      <path d="M220,1396 L940,1390 L948,1602 L176,1600 Q150,1560 168,1500 Z"/>
      <path d="M272,1632 L1040,1630 Q1050,1700 1040,1770 L270,1772 Z"/>
      <path d="M272,1778 L1070,1774 Q1078,1844 1070,1914 L266,1916 Z"/>
      <path d="M160,1964 L910,1960 L912,2180 L152,2176 Q140,2070 160,1964 Z"/>
    </g>
    <!-- food photos -->
    <ellipse role="img" aria-label="Photo of a grilled chicken wrap with slaw on a wooden board" cx="300" cy="1210" rx="282" ry="126" fill="var(--wood)"/>
    <path role="img" aria-label="Photo of a beetroot wrap with chicken and salad cut in half"
          d="M840,1430 Q900,1370 1090,1376 Q1170,1470 1160,1560 Q1060,1622 880,1600 Q820,1510 840,1430 Z" fill="var(--beet)"/>
    <path role="img" aria-label="Photo of roast chicken quarter with vegetable rice on a wooden plate"
          d="M60,1680 Q120,1620 360,1630 Q400,1720 380,1860 Q300,1910 130,1900 Q50,1800 60,1680 Z" fill="var(--wood)"/>
    <circle role="img" aria-label="Photo of roasted potatoes with thyme and garlic" cx="994" cy="2076" r="144" fill="var(--potato)"/>
  </svg>

  <h1 class="title">MENU</h1>

  <section class="item" style="left:600px; top:1104px; width:500px;">
    <div class="item__name">Ciabatta</div>
    <div class="item__desc">Roti Chicken, Rucola, Caramelized Onions.<br>Tomato, Fresh Onion</div>
    <div class="item__price" style="left:408px; top:-2px;">£6</div>
  </section>

  <section class="item" style="left:604px; top:1244px; width:500px;">
    <div class="item__name">Wrap</div>
    <div class="item__desc">Roti Chicken, Crunchy Slaw, Tomato,<br>Fresh Onion &amp; Sauce of your choice</div>
    <div class="item__price" style="left:416px; top:-2px;">£7</div>
  </section>

  <section class="item" style="left:290px; top:1446px; width:520px;">
    <div class="item__name" style="font-size:42px;">Beetroot Wrap</div>
    <div class="item__desc" style="font-size:27px; margin-top:10px;">Roti Chicken, Crunchy Slaw, Tomato,<br>Fresh Onion &amp; Sauce of your choice</div>
    <div class="item__price" style="left:430px; top:-2px; font-size:44px;">£8</div>
  </section>

  <section class="item item--box" style="left:434px; top:1680px; width:560px;">
    <div class="item__name">1/4 Chicken Box</div>
    <div class="item__price" style="left:470px; top:-2px;">£9</div>
  </section>

  <section class="item item--box" style="left:434px; top:1814px; width:560px;">
    <div class="item__name">1/2 Chicken Box</div>
    <div class="item__desc" style="font-size:26px;">Roti Chicken, Veggie Rice &amp; Salad</div>
    <div class="item__price" style="left:456px; top:-4px;">£14</div>
  </section>

  <section class="item item--side" style="left:234px; top:1990px; width:520px;">
    <div class="item__name">Roasted Potatoes</div>
    <div class="item__desc">Thyme &amp; Garlic</div>
    <div class="item__price" style="left:390px; top:-2px; font-size:38px;">£2.5</div>
  </section>

  <section class="item item--side" style="left:234px; top:2090px; width:520px;">
    <div class="item__name">Water</div>
    <div class="item__price" style="left:400px; top:-26px; font-size:38px;">£1</div>
  </section>

  <section class="item item--side" style="left:234px; top:2128px; width:520px;">
    <div class="item__name">Can &amp; Juices</div>
    <div class="item__price" style="left:382px; top:-2px; font-size:38px;">£1.8</div>
  </section>

  <footer class="footer">
    <h2 class="footer__title">SAUCES</h2>
    <ul class="sauce-list">
      <li>Signature</li><li>BBQ</li><li>Piri Piri</li>
      <li>Sweet Chilli</li><li>Garlic</li><li>Mayo</li>
    </ul>
  </footer>
</main>
</body>
</html>
```